Food Choices & Patient-Reported Outcomes in Parkinson's disease

We have spent the past 7 years studying food choices and rate of PD progression. We want to show people which foods have the most significant impact. <br/><br/>The infographic attached called "Community Wellness in QM" is the first in this 6-part series, recently designed by someone on PixelForge. I'd like this entire series to "pair nicely" with one another, but also have unique personality, which is why I've opened the contest up. <br/><br/>The VEX-QM scale is the point of reference, it explains that higher scores are worse, low scores are better. I'd like to stick with the green is good, red is bad theme. ish. <br/><br/>The blue bar chart with food is "the grand finale." THIS is the information people have been waiting for for decades! I expect this to be highly circulated-- passed to physicians, support groups, getting tens of thousands of shares online! Below, I uploaded the 2019 version (also produced by someone from Pixel Forge). On my ppt screen shot, that data on the bottom left is also REALLY important. Can make another bar chart? Or find some other creative way to communicate it? OK to not include the p-values (OK to remove the far right column). Thanks!

Target Market(s)

Patients, their partners/ families, and health care providers.

Requirements
Must have
• Must include the legend-- some version of the VEX-QM scale vs. Quality of Life, as a point of reference. If possible, I'd like to stick with [some shade of] green is good, with it being clear that scores are getting worse [red-ish] as the scores increase.
• Must have the website, so people can go look for more information/ details about the project.
Nice to have
• Coordination with the "Community Wellness ..." infographic below.

```html
<!DOCTYPE html>
<html lang="en">
<head>
<meta charset="utf-8">
<title>Food Choices &amp; Patient-Reported Outcomes in Parkinson's Disease</title>
<link rel="stylesheet" href="https://fonts.googleapis.com/css2?family=Mulish:wght@300;400;600;700;800&family=Cormorant+Garamond:wght@500;600&display=swap">
<style>
  :root {
    --navy: #535b92;
    --navy-deep: #2e3a8c;
    --sky: #c6d0e9;
    --pale: #e7eff9;
    --white: #ffffff;
    --teal-title: #3f6966;
    --poor: #f37b5f;
    --fair: #f7a67e;
    --good: #c1dea2;
    --excellent: #93c96b;
    --red: #f26b50;
    --green: #7dc35b;
    --track: #e6e6e6;
    --ink: #3a3a3a;
    --grey: #8c8c8c;
    --steel: #6d8cb3;
    --olive: #5b5b4f;
    --lime: #d8e122;
    --orange: #ef5a2a;
  }
  * { margin: 0; padding: 0; box-sizing: border-box; }
  html, body { width: 1200px; height: 848px; overflow: hidden; background: var(--navy); }
  body { font-family: 'Mulish', sans-serif; position: relative; }

  .right-field { position: absolute; left: 694px; top: 0; width: 506px; height: 848px; background: var(--sky); }
  .main-title { position: absolute; left: 40px; top: 30px; color: var(--white); font-size: 30px; line-height: 36px; font-weight: 300; }
  .main-title b { font-weight: 800; }
  .year { position: absolute; left: 555px; top: 44px; color: var(--white); font-size: 31px; font-weight: 800; }
  .side-title { position: absolute; right: 40px; top: 42px; text-align: right; color: var(--teal-title); font-size: 27px; line-height: 31px; font-weight: 400; }
  .side-title b { font-weight: 800; }

  .quality-panel { position: absolute; left: 16px; top: 120px; width: 678px; height: 378px; background: var(--white); }
  .behavior-panel { position: absolute; left: 16px; top: 498px; width: 678px; height: 338px; background: var(--pale); }
  .behavior-tab { position: absolute; left: 70px; top: 499px; width: 624px; height: 38px; background: var(--navy); border-radius: 30px 0 0 0;
    color: var(--white); font-family: 'Cormorant Garamond', serif; font-size: 25px; font-weight: 500; letter-spacing: 0.6px; text-align: center; line-height: 38px; }
  .servings-panel { position: absolute; left: 708px; top: 120px; width: 460px; height: 690px; background: var(--white); }
  .site-footer { position: absolute; left: 702px; top: 809px; width: 498px; height: 39px; background: var(--navy); border-radius: 34px 0 0 0;
    color: var(--white); font-size: 21px; letter-spacing: 1.4px; line-height: 40px; text-align: right; padding-right: 48px; }

  .chart { position: absolute; left: 0; top: 0; }
  .serif-head { font-family: 'Cormorant Garamond', serif; font-weight: 500; }
</style>
</head>
<body>
  <div class="right-field"></div>
  <h1 class="main-title">Food Choices &amp; Patient-<b>Reported</b><br><b>Outcomes in Parkinson's Disease</b></h1>
  <div class="year">2020</div>
  <h2 class="side-title">Impact of <b>2-4 Servings Per Week</b><br>On Parkinson's Disease Severity</h2>

  <section class="quality-panel"></section>
  <section class="behavior-panel"></section>
  <div class="behavior-tab">Impact of dietary behaviors on PD progression</div>
  <section class="servings-panel"></section>
  <footer class="site-footer">www.eatingwellstudyhub.org</footer>

  <!-- quality of life scale -->
  <svg class="chart" width="1200" height="848" viewBox="0 0 1200 848" role="img" aria-label="Scatter chart of VEX-QM score against years since diagnosis">
    <text x="362" y="152" text-anchor="middle" class="serif-head" font-size="25" fill="#555" letter-spacing="1.2">Correlation between Quality of life &amp; VEX-QM score</text>
    <g class="bands">
      <rect x="126" y="168" width="354" height="102" fill="var(--poor)"/>
      <rect x="126" y="270" width="354" height="50" fill="var(--fair)"/>
      <rect x="126" y="320" width="354" height="56" fill="var(--good)"/>
      <rect x="126" y="376" width="354" height="48" fill="var(--excellent)"/>
    </g>
    <g stroke="#fff" stroke-width="2" opacity="0.85">
      <line x1="176.6" y1="168" x2="176.6" y2="424"/><line x1="227.2" y1="168" x2="227.2" y2="424"/>
      <line x1="277.8" y1="168" x2="277.8" y2="424"/><line x1="328.4" y1="168" x2="328.4" y2="424"/>
      <line x1="379" y1="168" x2="379" y2="424"/><line x1="429.6" y1="168" x2="429.6" y2="424"/>
      <line x1="126" y1="218" x2="480" y2="218"/><line x1="126" y1="270" x2="480" y2="270"/>
      <line x1="126" y1="320" x2="480" y2="320"/><line x1="126" y1="376" x2="480" y2="376"/>
    </g>
    <g fill="#fff">
      <circle cx="130" cy="190" r="2"/><circle cx="148" cy="205" r="2"/><circle cx="160" cy="250" r="2"/><circle cx="185" cy="212" r="2"/>
      <circle cx="205" cy="200" r="2"/><circle cx="232" cy="198" r="2"/><circle cx="240" cy="238" r="2"/><circle cx="258" cy="258" r="2"/>
      <circle cx="275" cy="224" r="2"/><circle cx="302" cy="236" r="2"/><circle cx="340" cy="210" r="2"/><circle cx="365" cy="244" r="2"/>
      <circle cx="298" cy="198" r="2"/><circle cx="214" cy="242" r="2"/><circle cx="170" cy="232" r="2"/><circle cx="138" cy="258" r="2"/>
      <circle cx="132" cy="278" r="2"/><circle cx="140" cy="286" r="2"/><circle cx="150" cy="276" r="2"/><circle cx="158" cy="292" r="2"/>
      <circle cx="168" cy="282" r="2"/><circle cx="178" cy="298" r="2"/><circle cx="190" cy="284" r="2"/><circle cx="202" cy="296" r="2"/>
      <circle cx="214" cy="280" r="2"/><circle cx="228" cy="290" r="2"/><circle cx="244" cy="302" r="2"/><circle cx="262" cy="286" r="2"/>
      <circle cx="284" cy="298" r="2"/><circle cx="300" cy="282" r="2"/><circle cx="322" cy="306" r="2"/><circle cx="350" cy="292" r="2"/>
      <circle cx="132" cy="304" r="2"/><circle cx="146" cy="312" r="2"/><circle cx="134" cy="326" r="2"/><circle cx="152" cy="332" r="2"/>
      <circle cx="164" cy="318" r="2"/><circle cx="176" cy="336" r="2"/><circle cx="188" cy="326" r="2"/><circle cx="200" cy="344" r="2"/>
      <circle cx="212" cy="330" r="2"/><circle cx="226" cy="348" r="2"/><circle cx="240" cy="334" r="2"/><circle cx="256" cy="352" r="2"/>
      <circle cx="272" cy="338" r="2"/><circle cx="292" cy="356" r="2"/><circle cx="318" cy="342" r="2"/><circle cx="344" cy="360" r="2"/>
      <circle cx="372" cy="348" r="2"/><circle cx="392" cy="334" r="2"/><circle cx="130" cy="352" r="2"/><circle cx="142" cy="364" r="2"/>
      <circle cx="156" cy="356" r="2"/><circle cx="168" cy="370" r="2"/><circle cx="182" cy="360" r="2"/><circle cx="196" cy="374" r="2"/>
      <circle cx="130" cy="384" r="2"/><circle cx="140" cy="396" r="2"/><circle cx="152" cy="388" r="2"/><circle cx="162" cy="402" r="2"/>
      <circle cx="174" cy="392" r="2"/><circle cx="186" cy="408" r="2"/><circle cx="198" cy="396" r="2"/><circle cx="212" cy="390" r="2"/>
      <circle cx="226" cy="404" r="2"/><circle cx="134" cy="414" r="2"/><circle cx="148" cy="418" r="2"/><circle cx="244" cy="392" r="2"/>
      <circle cx="278" cy="388" r="2"/><circle cx="310" cy="400" r="2"/><circle cx="356" cy="412" r="2"/><circle cx="230" cy="414" r="2"/>
      <circle cx="136" cy="340" r="2"/><circle cx="144" cy="372" r="2"/><circle cx="160" cy="344" r="2"/><circle cx="172" cy="308" r="2"/>
      <circle cx="464" cy="284" r="2"/><circle cx="342" cy="256" r="2"/><circle cx="396" cy="214" r="2"/>
    </g>
    <line x1="126" y1="365" x2="480" y2="252" stroke="var(--navy-deep)" stroke-width="3"/>
    <g font-family="Mulish, sans-serif" font-weight="700" font-size="16" fill="var(--navy-deep)">
      <text x="383" y="246">POOR</text><text x="383" y="303">FAIR</text>
      <text x="383" y="346">GOOD</text><text x="383" y="393">EXCELLENT</text>
    </g>
    <g font-family="Cormorant Garamond, serif" font-weight="600" font-size="17" fill="#222" text-anchor="end">
      <text x="116" y="192">2,500</text><text x="116" y="229">2,000</text><text x="116" y="277">1,500</text>
      <text x="116" y="324">1,000</text><text x="116" y="373">500</text>
    </g>
    <g font-family="Cormorant Garamond, serif" font-weight="600" font-size="17" fill="#222" text-anchor="middle">
      <text x="169" y="454">5</text><text x="223" y="454">10</text><text x="273" y="454">15</text><text x="324" y="454">20</text>
      <text x="374" y="454">25</text><text x="426" y="454">30</text><text x="475" y="454">35</text>
    </g>
    <text x="290" y="478" text-anchor="middle" font-family="Mulish, sans-serif" font-size="14" fill="#a6a6a6">Years Since Diagnosis</text>
    <text transform="translate(50 285) rotate(-90)" text-anchor="middle" font-family="Mulish, sans-serif" font-size="12" fill="#a6a6a6" letter-spacing="0.5">VEX-QM SCORE</text>

    <g font-family="Mulish, sans-serif">
      <rect x="496" y="178" width="16" height="16" fill="var(--red)"/>
      <text x="522" y="192" font-size="16" font-weight="700" fill="var(--red)">HIGHER VEX-QM</text>
      <g fill="var(--red)"><circle cx="516" cy="214" r="2.2"/><circle cx="516" cy="234" r="2.2"/><circle cx="516" cy="254" r="2.2"/><circle cx="516" cy="274" r="2.2"/><circle cx="516" cy="296" r="2.2"/></g>
      <g font-size="10" font-weight="600" fill="#555" letter-spacing="1">
        <text x="530" y="218">DAIRY</text><text x="530" y="238">BEEF</text><text x="530" y="258">CANNED FRUITS &amp; VEGGIES</text>
        <text x="530" y="278">FRIED FOODS</text><text x="530" y="300">SODA</text>
      </g>
      <rect x="496" y="317" width="16" height="16" fill="var(--green)"/>
      <text x="522" y="331" font-size="16" font-weight="700" fill="var(--green)">LOWER VEX-QM</text>
      <g fill="var(--green)"><circle cx="516" cy="352" r="2.2"/><circle cx="516" cy="386" r="2.2"/><circle cx="516" cy="406" r="2.2"/><circle cx="516" cy="429" r="2.2"/><circle cx="516" cy="450" r="2.2"/><circle cx="516" cy="474" r="2.2"/></g>
      <g font-size="10" font-weight="600" fill="#555" letter-spacing="1">
        <text x="530" y="356">FRESH FRUITS</text><text x="530" y="368">&amp; VEGGIES</text><text x="530" y="390">NUTS &amp; SEEDS</text>
        <text x="530" y="410">OLIVE &amp; COCONUT OIL</text><text x="530" y="433">FRESH HERB &amp; SPICES</text>
        <text x="530" y="454">NON-FRIED FISH</text><text x="530" y="478">WINE</text>
      </g>
    </g>
  </svg>

  <!-- dietary behaviors -->
  <svg class="chart" width="1200" height="848" viewBox="0 0 1200 848" role="img" aria-label="Bar chart of dietary behaviors and their impact on progression">
    <line x1="485" y1="545" x2="485" y2="814" stroke="#d4dceb" stroke-width="1"/>
    <g font-family="Mulish, sans-serif" font-size="11.5" fill="#333" text-anchor="end">
      <text x="342" y="557">I cook most of my meals</text>
      <text x="342" y="578">I avoid artificial sweetners</text>
      <text x="342" y="598">I avoid soda</text>
      <text x="342" y="622">I avoid artificial colors, flavors</text>
      <text x="342" y="646">I routinely prepare meals for others</text>
      <text x="342" y="669">I avoid dairy</text>
      <text x="342" y="691">I try to eat organically grown foods when possible</text>
      <text x="342" y="714">I avoid pork</text>
      <text x="342" y="736">I buy from local farmers</text>
      <text x="342" y="758">I avoid beef</text>
      <text x="342" y="782" fill="var(--orange)">I find it difficult to afford healthy food</text>
      <text x="342" y="804" fill="var(--orange)">It is difficult to afford groceries</text>
    </g>
    <g font-family="Mulish, sans-serif" font-size="15" fill="var(--steel)">
      <text x="355" y="559">-146</text><text x="355" y="580">-121</text><text x="355" y="600">-108</text>
      <text x="355" y="624">-106</text><text x="355" y="648">-105</text><text x="355" y="671">-92</text>
      <text x="355" y="693">-86</text><text x="355" y="716">-75</text><text x="355" y="738">-71</text>
      <text x="355" y="760">-63</text><text x="355" y="784" fill="var(--orange)">366</text><text x="355" y="806" fill="var(--orange)">389</text>
    </g>
    <g fill="var(--olive)">
      <rect x="390" y="548" width="95" height="10"/><rect x="390" y="569" width="95" height="10"/><rect x="390" y="589" width="95" height="10"/>
      <rect x="390" y="613" width="95" height="10"/><rect x="390" y="637" width="95" height="10"/><rect x="390" y="660" width="95" height="10"/>
      <rect x="390" y="682" width="95" height="10"/><rect x="390" y="705" width="95" height="10"/><rect x="390" y="727" width="95" height="10"/>
      <rect x="390" y="749" width="95" height="10"/><rect x="485" y="773" width="95" height="10"/><rect x="485" y="795" width="95" height="10"/>
    </g>
    <g fill="var(--lime)">
      <rect x="450" y="548" width="35" height="10"/><rect x="456" y="569" width="29" height="10"/><rect x="459" y="589" width="26" height="10"/>
      <rect x="460" y="613" width="25" height="10"/><rect x="460" y="637" width="25" height="10"/><rect x="463" y="660" width="22" height="10"/>
      <rect x="465" y="682" width="20" height="10"/><rect x="467" y="705" width="18" height="10"/><rect x="468" y="727" width="17" height="10"/>
      <rect x="470" y="749" width="15" height="10"/>
    </g>
    <g fill="var(--orange)"><rect x="485" y="773" width="87" height="10"/><rect x="485" y="795" width="92" height="10"/></g>
    <g font-family="Mulish, sans-serif" font-size="9" fill="#c5d2e6" text-anchor="middle">
      <text x="390" y="829">-400</text><text x="434" y="829">-200</text><text x="485" y="829">0</text><text x="534" y="829">200</text><text x="582" y="829">400</text>
    </g>
  </svg>

  <!-- servings per week -->
  <svg class="chart" width="1200" height="848" viewBox="0 0 1200 848" role="img" aria-label="Bar chart of food servings and disease severity">
    <g font-family="Mulish, sans-serif" font-size="11" font-weight="700" text-anchor="middle">
      <text x="838" y="141" fill="var(--green)">-300</text><text x="892" y="141" fill="var(--green)">-150</text><text x="942" y="141" fill="#999">0</text>
    </g>
    <g fill="var(--track)">
      <rect x="840" y="161" width="104" height="11"/><rect x="840" y="188" width="104" height="11"/><rect x="840" y="213" width="104" height="11"/>
      <rect x="840" y="241" width="104" height="11"/><rect x="840" y="266" width="104" height="11"/><rect x="840" y="292" width="104" height="11"/>
      <rect x="840" y="318" width="104" height="11"/><rect x="840" y="344" width="104" height="11"/>
    </g>
    <g fill="var(--green)">
      <rect x="866" y="161" width="78" height="11"/><rect x="879" y="188" width="65" height="11"/><rect x="888" y="213" width="56" height="11"/>
      <rect x="894" y="241" width="50" height="11"/><rect x="904" y="266" width="40" height="11"/><rect x="904" y="292" width="40" height="11"/>
      <rect x="917" y="318" width="27" height="11"/><rect x="924" y="344" width="20" height="11"/>
    </g>
    <g font-family="Mulish, sans-serif" font-size="16" fill="var(--green)">
      <text x="950" y="172">-225</text><text x="950" y="199">-188</text><text x="950" y="224">-161</text><text x="950" y="252">-144</text>
      <text x="950" y="277">-115</text><text x="950" y="303">-114</text><text x="950" y="329">-79</text><text x="950" y="355">-58</text>
    </g>
    <g font-family="Mulish, sans-serif" font-size="14" fill="#444" letter-spacing="0.8">
      <text x="990" y="171">FRESH VEGETABLES</text><text x="990" y="198">FRESH FRUITS</text><text x="990" y="223">NUTS/SEEDS</text>
      <text x="990" y="251">FISH</text><text x="990" y="276">WINE</text><text x="990" y="302">OLIVE OIL</text>
      <text x="990" y="328">COCONUT OIL</text><text x="990" y="354">FRESH HERBS</text>
    </g>

    <g fill="var(--track)">
      <rect x="944" y="370" width="104" height="11"/><rect x="944" y="397" width="104" height="11"/><rect x="944" y="422" width="104" height="11"/>
      <rect x="944" y="449" width="104" height="11"/><rect x="944" y="475" width="104" height="11"/><rect x="944" y="501" width="104" height="11"/>
      <rect x="944" y="527" width="104" height="11"/><rect x="944" y="553" width="104" height="11"/><rect x="944" y="580" width="104" height="11"/>
      <rect x="944" y="606" width="104" height="11"/><rect x="944" y="633" width="104" height="11"/><rect x="944" y="659" width="104" height="11"/>
      <rect x="944" y="685" width="104" height="11"/><rect x="944" y="711" width="104" height="11"/><rect x="944" y="737" width="104" height="11"/>
    </g>
    <g fill="var(--red)">
      <rect x="944" y="370" width="15" height="11"/><rect x="944" y="397" width="18" height="11"/><rect x="944" y="422" width="20" height="11"/>
      <rect x="944" y="449" width="22" height="11"/><rect x="944" y="475" width="23" height="11"/><rect x="944" y="501" width="24" height="11"/>
      <rect x="944" y="527" width="24" height="11"/><rect x="944" y="553" width="29" height="11"/><rect x="944" y="580" width="30" height="11"/>
      <rect x="944" y="606" width="37" height="11"/><rect x="944" y="633" width="38" height="11"/><rect x="944" y="659" width="42" height="11"/>
      <rect x="944" y="685" width="50" height="11"/><rect x="944" y="711" width="51" height="11"/><rect x="944" y="737" width="66" height="11"/>
    </g>
    <g font-family="Mulish, sans-serif" font-size="16" fill="var(--red)">
      <text x="914" y="382">42</text><text x="914" y="408">51</text><text x="914" y="433">56</text><text x="914" y="460">63</text>
      <text x="914" y="486">67</text><text x="914" y="512">68</text><text x="914" y="538">69</text><text x="914" y="564">84</text>
      <text x="914" y="591">86</text><text x="914" y="617">106</text><text x="914" y="644">110</text><text x="914" y="670">120</text>
      <text x="914" y="696">144</text><text x="914" y="722">146</text><text x="914" y="748">191</text>
    </g>
    <g font-family="Mulish, sans-serif" font-size="13" fill="#444" letter-spacing="0.8" text-anchor="end">
      <text x="900" y="381">MILK</text><text x="900" y="407">CHEESE</text><text x="900" y="432">YOGURT</text>
      <text x="900" y="459">FROZEN VEGETABLES</text><text x="900" y="485">PORK</text><text x="900" y="511">CHICKEN</text>
      <text x="900" y="537">PLASTIC-BOTTLED DRINKS</text><text x="900" y="563">SODA</text><text x="900" y="590">PASTA</text>
      <text x="900" y="616">BEEF</text><text x="900" y="643">CANNED VEG</text><text x="900" y="669">ICE CREAM</text>
      <text x="900" y="695">FRIED FOODS</text><text x="900" y="721">DIET SODA</text><text x="900" y="747">CANNED FRUIT</text>
    </g>
    <g font-family="Mulish, sans-serif" font-size="11" font-weight="700" text-anchor="middle">
      <text x="942" y="770" fill="#999">0</text><text x="996" y="770" fill="var(--red)">150</text><text x="1050" y="770" fill="var(--red)">300</text>
    </g>
    <g font-family="Mulish, sans-serif" font-size="9" fill="#a9cbe8" text-anchor="middle">
      <text x="944" y="783">Never</text><text x="944" y="795">Consume</text>
    </g>
  </svg>
</body>
</html>
```